Business card design for a dynamic IT consulting company

We need a business card design for a young firm, specialized in the Telecommunications/Consulting industry. The name of the company is Brask and Partners Business Consulting Ltd. (Short name: Brask and Partnes)
Brask = solve read reverse, so we aim to be uncomplicated and solution-oriented. The small pipe in our logo is also related to the word solve. So we need a new business card design, which is simple, eye catching and something non traditional (I would probably prefer a square shaped design rather than a rectangle, but open for suggestions). Attached our logo.

Target Market(s)

Usually our customers are Tier1 Telecoms providers (Q-Linkra, Parnexo, etc) and their executives.

Industry/Entity Type

Business

Contact Information for Business Card

Name: Gergely Halmindo
Email: g.halmindo@braskpartnera.hu
Web: www.braskpartnera.hu
Mobile: +36 30 555 0192
Title: Managing Director

Optional:
Company name: Brask and Partners Ltd.
Address: 1047 Budapest, Ravaszi str. 17/B, Hungary

Font styles to use
Other font styles liked:
• helveticaneue_medium, Prime Regular are used now.

Colors

Designer to choose colors to be used in the design.

Requirements
Must have
• I would like to have a 2 sided design.
Nice to have
• I thought if we make the logo a bit bigger (without the company name), that could go to the back with the company name below. I though, if the pipe in the logo is somehow touchable on the business card, would be nice and unique.

```html
<!DOCTYPE html>
<html lang="en">
<head>
<meta charset="utf-8">
<title>Brask &amp; Partners – Business Card</title>
<link rel="stylesheet" href="https://fonts.googleapis.com/css2?family=Exo+2:wght@400;500&family=Arimo:wght@700&display=swap">
<style>
  :root {
    --page: #ffffff;
    --red: #fb0a10;
    --red-bright: #ff1a22;
    --red-dark: #c8082f;
    --red-side: #e20d16;
    --ink: #0b0b0c;
    --slate: #4a4f56;
    --title: #1f1f1f;
    --white: #ffffff;
  }
  * { box-sizing: border-box; margin: 0; padding: 0; }
  html, body { width: 1200px; height: 1000px; overflow: hidden; background: var(--page); }
  .canvas { position: relative; width: 1200px; height: 1000px; }

  .card { position: absolute; overflow: hidden; box-shadow: 0 2px 10px rgba(0,0,0,0.35); }
  .card svg.shapes { position: absolute; inset: 0; }
  .card-front { left: 231px; top: 28px; width: 773px; height: 441px; background: var(--white); }
  .card-back { left: 222px; top: 513px; width: 775px; height: 464px; background: var(--red); }

  .brand { position: absolute; display: flex; align-items: center; gap: 14px;
           font-family: "Exo 2", sans-serif; font-weight: 400; white-space: nowrap; }
  .brand-square { display: block; width: 34px; height: 34px; }
  .brand-front { left: 180px; top: 22px; font-size: 42px; color: var(--slate); }
  .brand-front .brand-square { background: var(--slate); }
  .brand-back { left: 205px; top: 192px; font-size: 36px; color: var(--white); }
  .brand-back .brand-square { width: 28px; height: 28px; background: var(--white); }

  .specialty { position: absolute; left: 0; width: 100%; top: 84px; text-align: center;
               font-family: "Exo 2", sans-serif; font-size: 24px; color: var(--red); }

  .person-name { position: absolute; left: 226px; top: 128px; font-family: "Exo 2", sans-serif;
                 font-size: 35px; color: var(--white); white-space: nowrap; }
  .person-title { position: absolute; left: 257px; top: 172px; font-family: "Arimo", sans-serif;
                  font-weight: 700; font-size: 26px; color: var(--title); }

  .contact { position: absolute; display: flex; align-items: center; gap: 24px;
             font-family: "Exo 2", sans-serif; font-size: 22px; color: var(--slate); white-space: nowrap; }
  .contact .icon { width: 26px; height: 26px; background: var(--red); display: flex;
                   align-items: center; justify-content: center; }
  .contact-web { left: 214px; top: 244px; }
  .contact-phone { left: 247px; top: 277px; }
  .contact-mail { left: 280px; top: 310px; }
</style>
</head>
<body>
<div class="canvas">

  <section class="card card-front" aria-label="Business card front">
    <svg class="shapes" width="773" height="441" viewBox="0 0 773 441" aria-hidden="true">
      <defs>
        <linearGradient id="ribbonShadow" x1="0" y1="0" x2="0" y2="1">
          <stop offset="0" stop-color="#000" stop-opacity="0.18"/>
          <stop offset="1" stop-color="#000" stop-opacity="0"/>
        </linearGradient>
      </defs>
      <rect class="band-red" x="0" y="137" width="773" height="93" fill="var(--red)"/>
      <rect class="band-shadow" x="125" y="230" width="521" height="16" fill="url(#ribbonShadow)"/>
      <polygon class="ribbon-fold" points="125,137 152,119 152,212 125,230" fill="var(--red-dark)"/>
      <polygon class="ribbon-fold" points="646,137 619,119 619,212 646,230" fill="var(--red-dark)"/>
      <rect class="ribbon" x="152" y="119" width="467" height="93" fill="var(--red-bright)"/>
      <rect class="band-black" x="0" y="375" width="773" height="66" fill="var(--ink)"/>
      <g class="diamond">
        <polygon points="91,355 178,442 91,529 4,442" fill="var(--red)"/>
        <polygon points="91,377 156,442 91,507 26,442" fill="var(--ink)"/>
      </g>
      <g class="diamond">
        <polygon points="187,258 274,345 187,432 100,345" fill="var(--red)"/>
        <polygon points="187,280 252,345 187,410 122,345" fill="var(--ink)"/>
      </g>
    </svg>

    <div class="brand brand-front"><span class="brand-square"></span>Brask &amp; Partners</div>
    <p class="specialty">specialized in the Telecommunications/Consulting industry</p>
    <h1 class="person-name">Gergely Halmindo</h1>
    <p class="person-title">Managing Director</p>

    <p class="contact contact-web">
      <span class="icon"><svg width="18" height="18" viewBox="0 0 18 18" aria-hidden="true"><g fill="none" stroke="#111" stroke-width="1.3"><circle cx="9" cy="9" r="7.5"/><ellipse cx="9" cy="9" rx="3.3" ry="7.5"/><line x1="1.5" y1="9" x2="16.5" y2="9"/><line x1="2.8" y1="5" x2="15.2" y2="5"/><line x1="2.8" y1="13" x2="15.2" y2="13"/></g></svg></span>
      www.braskpartnera.hu
    </p>
    <p class="contact contact-phone">
      <span class="icon"><svg width="18" height="18" viewBox="0 0 18 18" aria-hidden="true"><rect x="5" y="1.5" width="8" height="15" rx="1.5" fill="none" stroke="#111" stroke-width="1.5"/><line x1="7.5" y1="14" x2="10.5" y2="14" stroke="#111" stroke-width="1.3"/></svg></span>
      +36 30 555 0192
    </p>
    <p class="contact contact-mail">
      <span class="icon"><svg width="18" height="18" viewBox="0 0 18 18" aria-hidden="true"><rect x="2" y="4" width="14" height="10" fill="none" stroke="#111" stroke-width="1.4"/><polyline points="2,4 9,10 16,4" fill="none" stroke="#111" stroke-width="1.4"/></svg></span>
      g.halmindo@braskpartnera.hu
    </p>
  </section>

  <section class="card card-back" aria-label="Business card back">
    <svg class="shapes" width="775" height="464" viewBox="0 0 775 464" aria-hidden="true">
      <defs>
        <linearGradient id="boxShadow" x1="0" y1="0" x2="0" y2="1">
          <stop offset="0" stop-color="#7a0000" stop-opacity="0.35"/>
          <stop offset="1" stop-color="#7a0000" stop-opacity="0"/>
        </linearGradient>
      </defs>
      <polygon class="stripe" points="578,0 673,0 775,127 775,247" fill="var(--white)"/>
      <polygon class="stripe" points="0,220 196,464 103,464 0,337" fill="var(--white)"/>
      <rect class="box-shadow" x="123" y="307" width="505" height="22" fill="url(#boxShadow)"/>
      <polygon class="box-side" points="123,155 195,138 195,307 123,322" fill="var(--red-side)"/>
      <polygon class="box-side" points="628,155 556,138 556,307 628,322" fill="var(--red-side)"/>
      <rect class="box-face" x="195" y="138" width="361" height="169" fill="var(--red-bright)"/>
    </svg>
    <div class="brand brand-back"><span class="brand-square"></span>Brask &amp; Partners</div>
  </section>

</div>
</body>
</html>
```